Landscape Company in need of logo and business card update. Current logo file is attached.

I need a business card design for a Woman Owned Landscape business in Kansas City. I do Native plant installation and maintenance as well as mowing, chemical applications and residential and commercial landscaping.
My colors are navy, green and white.
I currently have a logo that can be used or you can redesign it.

Target Market(s)

Residential and commercial

Industry/Entity Type

Landscape

Contact Information for Business Card

On back of current card it lists what I do and website:
BMP/Raingarden Maintenance and Installation, Certified Chemical Applicator for Trees, shrubs, and turf; Landscape Design and Installation for residential and commercial.

Logo Text

Birchwell Landscape Partners, LLC

Font styles to use
Other font styles liked:
• See current font on logo examples

Requirements
Must have
• Phone number: 913-555-0182
• Website: www.birchwellyards.example
• Colors: Navy, Green, white
• Email: birchwellyards@mailbox.example
• Address: PO BOX 417208 Larkfield, KS 66099
• Name of Person: Marlene Kozik, owner

```html
<!DOCTYPE html>
<html lang="en">
<head>
<meta charset="utf-8">
<title>Birchwell Landscape Partners — Business Card</title>
<link rel="stylesheet" href="https://fonts.googleapis.com/css2?family=Quicksand:wght@400;500;700&display=swap">
<style>
  :root {
    --page: #ecece8;
    --card-white: #ffffff;
    --lime: #8cc63f;
    --lime-deep: #6fae2c;
    --forest: #2f6b2a;
    --night-green: #0e2411;
    --reed-green: #2c5a26;
    --ink-grey: #555b55;
    --shadow: rgba(0, 0, 0, 0.18);
  }
  * { box-sizing: border-box; margin: 0; padding: 0; }
  html, body {
    width: 1200px; height: 1040px; overflow: hidden;
    background: var(--page);
    font-family: "Quicksand", sans-serif;
  }
  .sheet {
    width: 1200px; height: 1040px;
    display: flex; flex-direction: column;
    align-items: center; justify-content: center; gap: 70px;
  }
  .card {
    width: 700px; height: 400px; position: relative; overflow: hidden;
    box-shadow: 0 10px 30px var(--shadow);
  }

  /* Front */
  .card-front { background: var(--card-white); }
  .contact-block {
    position: absolute; left: 190px; top: 56px;
    color: var(--ink-grey);
  }
  .owner-name {
    font-weight: 700; font-size: 30px; color: var(--forest); letter-spacing: 0.2px;
  }
  .owner-role { font-size: 17px; margin: 2px 0 0 50px; color: var(--ink-grey); }
  .contact-line {
    display: flex; align-items: center; gap: 10px;
    font-size: 19px; margin-top: 10px;
  }
  .contact-line.phone { margin-left: 50px; margin-top: 6px; }
  .contact-line.address { margin-top: 26px; }
  .contact-icon { width: 16px; height: 16px; flex: none; }
  .grass-band {
    position: absolute; left: 0; right: 0; bottom: 0; height: 150px;
    background: linear-gradient(to bottom, rgba(140,198,63,0) 0%, var(--lime) 38%, var(--lime-deep) 100%);
  }
  .services {
    position: absolute; left: 60px; right: 40px; bottom: 22px;
    color: var(--card-white); font-weight: 500; font-size: 15.5px; line-height: 1.4;
    text-align: center;
  }

  /* Back */
  .card-back { background: var(--night-green); }
  .brand-name {
    position: absolute; left: 60px; top: 110px; width: 400px;
    color: var(--lime); font-weight: 700; font-size: 44px; line-height: 1.12;
  }
  .brand-web {
    position: absolute; left: 60px; bottom: 44px;
    color: var(--lime); font-weight: 500; font-size: 18px;
  }
  .cattail-art {
    position: absolute; right: 0; bottom: 0; width: 260px; height: 260px;
    background: radial-gradient(ellipse at 60% 100%, var(--reed-green) 0%, rgba(44,90,38,0.6) 45%, rgba(14,36,17,0) 75%);
  }
</style>
</head>
<body>
<main class="sheet">

  <section class="card card-front" aria-label="Business card front">
    <div class="contact-block">
      <h1 class="owner-name">Marlene Kozik</h1>
      <p class="owner-role">owner</p>
      <p class="contact-line phone">
        <svg class="contact-icon" viewBox="0 0 16 16" aria-hidden="true"><path d="M4 1.5l2 3-1.3 1.4a8 8 0 0 0 5.4 5.4L11.5 10l3 2-1.2 2.3C8 14.5 1.5 8 1.7 2.7z" fill="var(--lime)"/></svg>
        913-555-0182
      </p>
      <p class="contact-line address">
        <svg class="contact-icon" viewBox="0 0 16 16" aria-hidden="true"><path d="M8 1a5 5 0 0 0-5 5c0 4 5 9 5 9s5-5 5-9a5 5 0 0 0-5-5z" fill="var(--lime)"/><circle cx="8" cy="6" r="2" fill="#fff"/></svg>
        PO BOX 417208 Larkfield, KS 66099
      </p>
      <p class="contact-line email">
        <svg class="contact-icon" viewBox="0 0 16 16" aria-hidden="true"><rect x="1" y="3" width="14" height="10" fill="var(--lime)"/><path d="M1.5 3.5L8 9l6.5-5.5" stroke="#fff" stroke-width="1.4" fill="none"/></svg>
        birchwellyards@mailbox.example
      </p>
    </div>
    <div class="grass-band" role="img" aria-label="Green grass silhouette along the bottom edge"></div>
    <p class="services">BMP/Raingarden Maintenance and Installation, Certified Chemical Applicator for Trees, shrubs, and turf; Landscape Design and Installation for residential and commercial.</p>
  </section>

  <section class="card card-back" aria-label="Business card back">
    <h2 class="brand-name">Birchwell Landscape Partners, LLC</h2>
    <p class="brand-web">www.birchwellyards.example</p>
    <div class="cattail-art" role="img" aria-label="Cattail and prairie grass illustration"></div>
  </section>

</main>
</body>
</html>
```